SkyvornQ Business Cards and Stationary Design

Need a design for our business cards and stationary. I want to carry on the theme of the logo. I want the business cards to have a design on the back. I would like the business cards and the stationary to carry the same theme, design scheme, and branding

Target Market(s)

Airlines and Maintenance Facilities

Industry/Entity Type

Aviation

Contact Information for Business Card

Address: 4827 Tallowmere Lane, Marrowick Bay, Tessaline, 34951

Font styles to use
Serif
Sans Serif

Colors

Designer to choose colors to be used in the design.

```html
<!DOCTYPE html>
<html lang="en">
<head>
<meta charset="utf-8">
<title>SkyvornQ Business Cards</title>
<link rel="stylesheet" href="https://fonts.googleapis.com/css2?family=Montserrat:wght@400;500;600;700;800&display=swap">
<style>
  :root {
    --page: #eeeff1;
    --card-white: #fbfbfb;
    --navy: #27365a;
    --blue: #2f83b0;
    --ink: #2c2c30;
    --ink-soft: #4a4a50;
    --accent: #3a8fd0;
    --rule: #b9bcc2;
    --light: #f2f4f7;
  }
  * { box-sizing: border-box; margin: 0; padding: 0; }
  html, body { width: 1200px; height: 1121px; overflow: hidden; }
  body {
    background: var(--page);
    font-family: "Montserrat", sans-serif;
    display: flex;
    flex-direction: column;
    align-items: center;
    justify-content: center;
    gap: 60px;
  }
  .card {
    width: 840px;
    height: 480px;
    border-radius: 4px;
    box-shadow: 0 6px 18px rgba(30, 40, 60, 0.12);
    position: relative;
    overflow: hidden;
  }

  /* Front */
  .card-front {
    background: var(--card-white);
    display: flex;
    align-items: center;
  }
  .front-brand {
    width: 50%;
    display: flex;
    align-items: center;
    justify-content: center;
    gap: 18px;
  }
  .brand-name {
    font-weight: 700;
    letter-spacing: 0.14em;
    text-transform: uppercase;
    white-space: nowrap;
  }
  .front-brand .brand-name { font-size: 34px; color: var(--navy); }
  .brand-dot {
    width: 56px; height: 56px;
    border-radius: 50%;
    border: 6px solid var(--accent);
    flex: none;
  }
  .divider {
    width: 1px;
    height: 220px;
    background: var(--rule);
    flex: none;
  }
  .contact {
    padding-left: 46px;
    color: var(--ink-soft);
    font-size: 17px;
    line-height: 1.45;
    white-space: nowrap;
  }
  .person-name { font-size: 26px; font-weight: 800; color: var(--ink); letter-spacing: 0.01em; }
  .person-role { margin-bottom: 4px; }
  .address { margin-bottom: 10px; }
  .contact-list { list-style: none; }
  .contact-list li { display: flex; align-items: center; gap: 12px; }
  .contact-list svg { width: 18px; height: 18px; flex: none; stroke: var(--accent); fill: none; stroke-width: 1.6; }

  /* Back */
  .card-back {
    background: linear-gradient(200deg, var(--blue) 0%, #2b5a85 45%, var(--navy) 100%);
    display: flex;
    align-items: center;
    justify-content: center;
    color: var(--light);
  }
  .back-block { display: flex; flex-direction: column; align-items: flex-start; gap: 30px; }
  .back-brand { display: flex; align-items: center; gap: 22px; }
  .back-brand .brand-name { font-size: 46px; color: var(--light); }
  .back-brand .brand-dot { width: 76px; height: 76px; border: 8px solid var(--light); }
  .back-url { font-size: 19px; letter-spacing: 0.08em; padding-left: 4px; }
</style>
</head>
<body>
  <section class="card card-front">
    <div class="front-brand">
      <span class="brand-name">SkyvornQ</span>
      <span class="brand-dot"></span>
    </div>
    <div class="divider"></div>
    <div class="contact">
      <p class="person-name">Darian VOSS</p>
      <p class="person-role">CEO / Founder</p>
      <p class="address">4827 Tallowmere Lane<br>Marrowick Bay, Tessaline, 34951</p>
      <ul class="contact-list">
        <li><svg viewBox="0 0 20 20"><path d="M5 2h3l1.5 4-2 1.5a10 10 0 0 0 5 5l1.5-2 4 1.5v3a2 2 0 0 1-2 2A15 15 0 0 1 3 4a2 2 0 0 1 2-2z"/></svg>000.000.0000</li>
        <li><svg viewBox="0 0 20 20"><rect x="6" y="2" width="8" height="16" rx="1.5"/><line x1="9" y1="15" x2="11" y2="15"/></svg>000.000.0000</li>
        <li><svg viewBox="0 0 20 20"><rect x="2" y="4.5" width="16" height="11" rx="1"/><path d="M2 5l8 6 8-6"/></svg>darian@skyvornq.com</li>
        <li><svg viewBox="0 0 20 20"><circle cx="10" cy="10" r="8"/><ellipse cx="10" cy="10" rx="3.5" ry="8"/><line x1="2" y1="10" x2="18" y2="10"/></svg>www.skyvornq.com</li>
      </ul>
    </div>
  </section>

  <section class="card card-back">
    <div class="back-block">
      <div class="back-brand">
        <span class="brand-name">SkyvornQ</span>
        <span class="brand-dot"></span>
      </div>
      <p class="back-url">www.skyvornq.com</p>
    </div>
  </section>
</body>
</html>
```